BriarLoom Website Homepage Design

Please provide your idea of homepage for a hosting company. This project is for DESIGN only, no coding.

It must use/combine colors used in logo, clean, modern look.

Homepage must consist of at least 4 sections (example: testimonials, services, and so on. not necesarily all of them). We would like the navigation to be horizontal, but not mandatory.

You can include a preview of services page (optional, not a must).

Number of Pages Required

1 page

Font styles to use
Sans Serif

```html
<!DOCTYPE html>
<html lang="en">
<head>
<meta charset="utf-8">
<title>BriarLoom — Hosting</title>
<link href="https://fonts.googleapis.com/css2?family=Roboto:ital,wght@0,300;0,400;0,500;0,700;1,400&display=swap" rel="stylesheet">
<style>
:root{
  --blue:#0b7fd8;
  --blue-dark:#0a5fb3;
  --ink:#1b1b1b;
  --text:#4a4a4a;
  --soft:#f3f7fd;
  --white:#ffffff;
  --star:#f5b800;
  --black:#000000;
  --rule:#333333;
}
*{box-sizing:border-box;margin:0;padding:0}
html,body{width:1200px;height:4038px;overflow:hidden}
body{font-family:'Roboto',sans-serif;color:var(--text);background:var(--white);position:relative}
ul{list-style:none}
.abs{position:absolute}
.brand{font-weight:500;font-size:40px;color:var(--white);letter-spacing:1px;display:flex;align-items:center;gap:10px}
.brand .dot{width:18px;height:18px;border-radius:50%;background:var(--blue)}

/* hero */
.hero{left:0;top:0;width:1200px;height:620px;background:linear-gradient(100deg,#0c1a36 0%,#15305c 45%,#3a5f8c 75%,#5b7ea4 100%)}
.nav{left:448px;top:30px;display:flex;align-items:center;font-size:15px;color:var(--white)}
.nav a{color:var(--white);text-decoration:none;margin-right:66px}
.nav .active{border-bottom:2px solid var(--white);padding-bottom:3px}
.btn-outline{left:930px;top:16px;width:170px;height:46px;border:2px solid var(--white);border-radius:24px;color:var(--white);font-size:15px;display:flex;align-items:center;justify-content:center}
.hero-title{left:98px;top:236px;font-size:38px;line-height:46px;font-weight:700;color:var(--white)}
.hero-lead{left:100px;top:334px;font-size:19px;color:var(--white);font-weight:300}
.btn{background:var(--blue);color:var(--white);border-radius:26px;font-size:15px;font-weight:500;display:flex;align-items:center;justify-content:center}
.dots{left:564px;top:590px;display:flex;gap:8px}
.dots span{width:11px;height:11px;border:1.5px solid var(--white);border-radius:50%}
.dots span.on{background:var(--white)}

.sec-title{width:1200px;left:0;text-align:center;font-size:40px;font-weight:400;color:var(--ink)}
.sec-title b{color:var(--blue);font-weight:700}
.sec-sub{width:1200px;left:0;text-align:center;font-size:15px;color:var(--ink)}
.underline{height:3px;width:56px;background:var(--blue);left:572px}

.card{background:var(--white);box-shadow:0 3px 16px rgba(0,40,90,.1);border-radius:4px;text-align:center}
.card h3{font-size:21px;font-weight:500;color:var(--ink);margin-top:18px}
.card p{font-size:13.5px;line-height:26px;color:var(--text);padding:0 22px;margin-top:10px}
.more{font-size:14px;font-weight:700;color:var(--blue);text-decoration:underline;display:inline-block;margin-top:14px}

.about{left:0;top:1266px;width:1200px;height:586px;background:var(--soft)}
.about-title{left:647px;top:1392px;font-size:40px;font-weight:400;color:var(--ink)}
.about-title b{color:var(--blue);font-weight:700}

.trust{left:0;top:1852px;width:1200px;height:388px;background:linear-gradient(90deg,#0a5fb3,#1283dc 50%,#0a5fb3)}
.stat{text-align:center;color:var(--white);width:260px}
.stat b{display:block;font-size:30px;font-weight:700}
.stat span{font-size:13px}
.logos{left:99px;top:2181px;width:1002px;height:106px;background:var(--white);border-radius:4px;box-shadow:0 4px 18px rgba(0,40,90,.12);display:flex;justify-content:space-around;align-items:center;font-size:28px;font-weight:500;color:#777}

.testi{left:0;top:2287px;width:1200px;height:674px;background:var(--soft)}
.quote{background:var(--white);box-shadow:0 3px 14px rgba(0,40,90,.08);width:292px;height:316px;padding:26px 22px}
.quote .mark{font-size:90px;line-height:60px;height:44px;color:#d7dbe2;font-weight:700}
.quote p{font-style:italic;font-size:14.5px;line-height:24px;color:var(--text);margin-top:14px}
.person{display:flex;gap:10px;align-items:center;margin-top:14px}
.avatar{width:52px;height:52px;border-radius:50%;background:linear-gradient(135deg,#8ea6bf,#4f6479)}
.person b{font-weight:500;font-size:15px;color:var(--ink);display:block}
.stars{color:var(--star);font-size:19px;letter-spacing:1px}

.news{background:var(--white);border:1px solid #e4e8ee;width:321px;height:409px}
.news .ph{height:209px}
.news h4{font-size:18px;font-weight:700;color:var(--ink);line-height:22px;padding:18px 14px 0}
.news p{font-size:12.5px;line-height:22px;padding:8px 16px 0}
.news .more{margin:6px 16px 0}

.footer{left:0;top:3650px;width:1200px;height:388px;background:var(--black)}
.foot-col{color:var(--white)}
.foot-col h5{font-size:18px;font-weight:700;color:var(--white)}
.foot-col h5::after{content:"";display:block;width:22px;height:2px;background:var(--white);margin-top:6px}
.foot-col ul{font-size:14.5px;line-height:29px;margin-top:12px}
.svc li::before{content:"•";margin-right:16px}
.contact-row{display:flex;gap:14px;align-items:flex-start;font-size:14.5px;line-height:22px;margin-top:18px}
.ico{width:32px;height:32px;border-radius:50%;background:var(--white);flex:none;display:flex;align-items:center;justify-content:center}
.social{display:flex;gap:14px}
.social span{width:34px;height:34px;border-radius:50%;background:var(--white)}
.foot-text{left:99px;top:3778px;width:260px;font-size:14.5px;line-height:23px;color:var(--white)}
.foot-rule{left:99px;top:3958px;width:1002px;height:1px;background:var(--rule)}
.copy{left:0;top:3984px;width:1200px;text-align:center;font-size:14.5px;color:var(--white)}
</style>
</head>
<body>

<section class="abs hero" role="img" aria-label="Two engineers with a laptop in a server room"></section>
<div class="abs brand" style="left:99px;top:16px"><span class="dot"></span>BriarLoom</div>
<nav class="abs nav">
  <a class="active">HOME</a><a>ABOUT</a><a>SERVICE</a><a>TESTIMONIAL</a>
</nav>
<div class="abs btn-outline">CONTACT US</div>
<svg class="abs" style="left:60px;top:295px" width="20" height="34"><path d="M16 2 L3 17 L16 32" stroke="#fff" stroke-width="2" fill="none"/></svg>
<svg class="abs" style="left:1120px;top:295px" width="20" height="34"><path d="M4 2 L17 17 L4 32" stroke="#fff" stroke-width="2" fill="none"/></svg>
<h1 class="abs hero-title">BEST HOSTING PROVIDER<br>FOR YOUR BUSINESS</h1>
<p class="abs hero-lead">Lorem ipsum dolor sit amet, consectetur adipiscing</p>
<div class="abs btn" style="left:99px;top:382px;width:191px;height:48px">GET STARTED</div>
<div class="abs dots"><span class="on"></span><span></span><span></span><span></span></div>

<!-- what we do -->
<h2 class="abs sec-title" style="top:692px"><b>WHAT</b> WE DO</h2>
<p class="abs sec-sub" style="top:746px">The standard Lorem Ipsum passage, used since</p>
<div class="abs underline" style="top:771px"></div>

<div class="abs card" style="left:99px;top:807px;width:321px;height:365px">
  <svg width="92" height="92" viewBox="0 0 92 92" style="margin-top:38px" fill="none" stroke="#0b7fd8" stroke-width="2.5"><path d="M20 40 a16 16 0 0 1 14-22 a20 20 0 0 1 36 6 a13 13 0 0 1 2 26 H22"/><rect x="44" y="44" width="34" height="12"/><rect x="44" y="58" width="34" height="12"/><rect x="44" y="72" width="34" height="12"/><circle cx="26" cy="70" r="10"/><circle cx="26" cy="70" r="4"/></svg>
  <h3>SED UT PERSPICIATIS</h3>
  <p>Lorem ipsum dolor sit amet, consectdipiscing elit, sed do eiusmod tempor inciunt ut labore et dolore magna aliqua. Quis ipsum suspendisse ultrices gravida. Risus commodo</p>
  <a class="more">LEARN MORE &nbsp;»</a>
</div>
<div class="abs card" style="left:439px;top:807px;width:321px;height:365px">
  <svg width="92" height="92" viewBox="0 0 92 92" style="margin-top:38px" fill="none" stroke="#0b7fd8" stroke-width="2.5"><circle cx="44" cy="48" r="22"/><circle cx="44" cy="48" r="10"/><path d="M44 16v8M44 72v8M12 48h8M68 48h8M21 25l6 6M61 65l6 6M21 71l6-6M61 31l6-6"/><path d="M56 64V40M64 64V30M72 64V22"/></svg>
  <h3>SED UT PERSPICIATIS</h3>
  <p>Lorem ipsum dolor sit amet, consectdipiscing elit, sed do eiusmod tempor inciunt ut labore et dolore magna aliqua. Quis ipsum suspendisse ultrices gravida. Risus commodo</p>
  <a class="more">LEARN MORE &nbsp;»</a>
</div>
<div class="abs card" style="left:779px;top:807px;width:321px;height:365px">
  <svg width="92" height="92" viewBox="0 0 92 92" style="margin-top:38px" fill="none" stroke="#0b7fd8" stroke-width="2.5"><rect x="8" y="12" width="50" height="14"/><rect x="8" y="30" width="50" height="14"/><rect x="8" y="48" width="30" height="14"/><ellipse cx="64" cy="54" rx="20" ry="7"/><path d="M44 54v24c0 4 9 7 20 7s20-3 20-7V54M44 66c0 4 9 7 20 7s20-3 20-7"/></svg>
  <h3>SED UT PERSPICIATIS</h3>
  <p>Lorem ipsum dolor sit amet, consectdipiscing elit, sed do eiusmod tempor inciunt ut labore et dolore magna aliqua. Quis ipsum suspendisse ultrices gravida. Risus commodo</p>
  <a class="more">LEARN MORE &nbsp;»</a>
</div>

<!-- about -->
<section class="abs about"></section>
<div class="abs" role="img" aria-label="Woman with a tablet in a server room" style="left:116px;top:1352px;width:388px;height:388px;border-radius:50%;background:radial-gradient(circle at 60% 40%,#6b5a42,#1d2a3a 70%)"></div>
<div class="abs" role="img" aria-label="Two technicians with a laptop" style="left:414px;top:1604px;width:160px;height:160px;border-radius:50%;border:4px solid #fff;background:linear-gradient(135deg,#cfd8e4,#6d8299)"></div>
<h2 class="abs about-title"><b>ABOUT</b> BRIARLOOM</h2>
<div class="abs" style="left:647px;top:1451px;width:56px;height:3px;background:var(--blue)"></div>
<p class="abs" style="left:647px;top:1474px;width:440px;font-size:13.5px;line-height:24.5px">Lorem ipsum dolor sit amet, consectetur adipiscing elit, sed d smod tempor incididunt ut labore et dolore magna aliqua. Qui suspendisse ultrices gravida. Risus commodo viverra maecenas accumsan lacus vel facilisis. Lorem ipsum dolor sit amet, consectetur adipiscing elit, sed do eiusmod tempor incididunt ut labore et dolore magna aliqua. Quis ipsum suspendisse ultrices gravida. Risodo viverra maecenas accumsan lacus vel facilisis</p>
<div class="abs btn" style="left:647px;top:1667px;width:173px;height:47px">LEARN MORE</div>

<!-- trusted -->
<section class="abs trust"></section>
<div class="abs" style="left:233px;top:1955px;width:84px;height:2px;background:#fff"></div>
<div class="abs" style="left:885px;top:1955px;width:80px;height:2px;background:#fff"></div>
<h2 class="abs" style="left:0;top:1934px;width:1200px;text-align:center;font-size:34px;color:#fff;font-weight:400"><b>TRUSTED ALL OVER</b> THE WORLD</h2>
<div class="abs stat" style="left:69px;top:2026px"><b>14 OFFICES</b><span>around the world</span></div>
<div class="abs stat" style="left:334px;top:2026px"><b>$5 BIILLION</b><span>sent every month</span></div>
<div class="abs stat" style="left:590px;top:2026px"><b>7 MILLION</b><span>customers</span></div>
<div class="abs stat" style="left:857px;top:2026px"><b>$1.5 BILLION</b><span>saved by customer every year</span></div>
<div class="abs logos"><span>Corvane</span><span>Lumetra</span><span>Nexaro</span><span>Parvel</span><span>Quinta</span></div>

<!-- testimonials -->
<section class="abs testi"></section>
<div class="abs" style="left:117px;top:2316px;width:3px;height:162px;background:var(--blue)"></div>
<p class="abs" style="left:148px;top:2346px;font-size:12.5px;color:var(--blue)">SOME LOVELY FEEDBACK FROM OUR CLIENTS</p>
<h2 class="abs" style="left:148px;top:2376px;font-size:37px;line-height:40px;font-weight:400;color:#1b1b1b"><b>WHAT PEOPLE</b><br>ARE SAYING</h2>
<svg class="abs" style="left:951px;top:2396px" width="54" height="54"><circle cx="27" cy="27" r="26" fill="#fff"/><path d="M31 18 L22 27 L31 36" stroke="#555" stroke-width="2" fill="none"/></svg>
<svg class="abs" style="left:1013px;top:2396px" width="54" height="54"><circle cx="27" cy="27" r="26" fill="#0b7fd8"/><path d="M23 18 L32 27 L23 36" stroke="#fff" stroke-width="2" fill="none"/></svg>

<div class="abs quote" style="left:133px;top:2521px"><div class="mark">“</div><p>“Lorem ipsum dolor sit ametsectetur adipiscing elit, sed do eiusmd tempor incididunt ut labore et dolore magna aliqua. Quis ipsum suspendie ultrices gravida. Risus codo vivrra maecenas accumsan lacus vel facilisis.”</p><div class="person"><div class="avatar" role="img" aria-label="Client portrait"></div><div><b>Dana Reyes</b><span class="stars">★★★★★</span></div></div></div>
<div class="abs quote" style="left:445px;top:2546px"><div class="mark">“</div><p>“Lorem ipsum dolor sit ametsectetur adipiscing elit, sed do eiusmd tempor incididunt ut labore et dolore magna aliqua. Quis ipsum suspendie ultrices gravida. Risus codo vivrra maecenas accumsan lacus vel facilisis.”</p><div class="person"><div class="avatar" role="img" aria-label="Client portrait"></div><div><b>Dana Reyes</b><span class="stars">★★★★★</span></div></div></div>
<div class="abs quote" style="left:760px;top:2489px"><div class="mark">“</div><p>“Lorem ipsum dolor sit ametsectetur adipiscing elit, sed do eiusmd tempor incididunt ut labore et dolore magna aliqua. Quis ipsum suspendie ultrices gravida. Risus codo vivrra maecenas accumsan lacus vel facilisis.”</p><div class="person"><div class="avatar" role="img" aria-label="Client portrait"></div><div><b>Dana Reyes</b><span class="stars">★★★★★</span></div></div></div>
<div class="abs quote" style="left:1072px;top:2554px"><div class="mark">“</div><p>“Lorem ipsum dolor sit ametsectetur adipiscing elit, sed do eiusmd tempor incididunt ut labore et dolore magna aliqua. Quis ipsum suspendie ultrices gravida. Risus codo vivrra maecenas accumsan lacus vel facilisis.”</p><div class="person"><div class="avatar" role="img" aria-label="Client portrait"></div><div><b>Dana Reyes</b><span class="stars">★★★★★</span></div></div></div>

<!-- news -->
<h2 class="abs sec-title" style="top:3040px"><b>LATEST</b> NEWS</h2>
<p class="abs sec-sub" style="top:3094px">The standard Lorem Ipsum passage, used since</p>
<div class="abs underline" style="top:3119px"></div>

<div class="abs news" style="left:99px;top:3147px"><div class="ph" role="img" aria-label="Technician cabling a server rack" style="background:linear-gradient(135deg,#2b3440,#7f8894)"></div><h4>The standard Lorem Ipsum passfe, used since the 1500s</h4><p>Lorem ipsum dolor sit amet, consectetur adipiscing elit, sed do eiusmod tempor incididunt ut labore et dolore magna aliqua. Quis ipsum suspisse ultrices gravida.</p><a class="more">LEARN MORE &nbsp;»</a></div>
<div class="abs news" style="left:439px;top:3147px"><div class="ph" role="img" aria-label="Two engineers walking past server racks" style="background:linear-gradient(135deg,#10233f,#3c6b9c)"></div><h4>The standard Lorem Ipsum passfe, used since the 1500s</h4><p>Lorem ipsum dolor sit amet, consectetur adipiscing elit, sed do eiusmod tempor incididunt ut labore et dolore magna aliqua. Quis ipsum suspisse ultrices gravida.</p><a class="more">LEARN MORE &nbsp;»</a></div>
<div class="abs news" style="left:779px;top:3147px"><div class="ph" role="img" aria-label="Laptop showing charts in a data centre" style="background:linear-gradient(135deg,#0d1f4a,#3857a8)"></div><h4>The standard Lorem Ipsum passfe, used since the 1500s</h4><p>Lorem ipsum dolor sit amet, consectetur adipiscing elit, sed do eiusmod tempor incididunt ut labore et dolore magna aliqua. Quis ipsum suspisse ultrices gravida.</p><a class="more">LEARN MORE &nbsp;»</a></div>

<!-- footer -->
<footer class="abs footer"></footer>
<div class="abs brand" style="left:99px;top:3712px"><span class="dot"></span>BriarLoom</div>
<p class="abs foot-text">Lorem ipsum dolor sit , consectetur adipiscing elit, sed do eiusmod tempor incididunt ut</p>
<div class="abs social" style="left:100px;top:3862px"><span></span><span></span><span></span></div>

<div class="abs foot-col" style="left:438px;top:3712px"><h5>MENU</h5><ul><li>Home</li><li>About Us</li><li>Our Services</li><li>Testimonial</li><li>Careers</li><li>Contact Us</li></ul></div>
<div class="abs foot-col" style="left:631px;top:3712px"><h5>CONTACT US</h5>
  <div class="contact-row"><span class="ico"><svg width="16" height="18" viewBox="0 0 16 18"><path d="M8 1a6 6 0 0 1 6 6c0 4-6 10-6 10S2 11 2 7a6 6 0 0 1 6-6z" fill="#0b7fd8"/><circle cx="8" cy="7" r="2" fill="#fff"/></svg></span><span>48 Harbor Lane Fairview<br>USA 30417</span></div>
  <div class="contact-row"><span class="ico"><svg width="16" height="16" viewBox="0 0 16 16"><path d="M3 1l3 3-2 2c1 2 3 4 5 5l2-2 3 3-2 3C7 15 1 9 1 3z" fill="#0b7fd8"/></svg></span><span style="margin-top:5px">(555) 014 2290</span></div>
  <div class="contact-row"><span class="ico"><svg width="16" height="12" viewBox="0 0 16 12"><rect width="16" height="12" fill="#0b7fd8"/><path d="M0 0l8 6 8-6" stroke="#fff" fill="none"/></svg></span><span style="margin-top:5px">info@briarloom.com</span></div>
</div>
<div class="abs foot-col" style="left:956px;top:3712px"><h5>SERVICES</h5><ul class="svc"><li>The standard</li><li>Sed ut perspiciati</li><li>Lorem Ipsum</li><li>Lorem Ipsum</li><li>Sed ut perspiciatis</li><li>Lorem Ipsum</li></ul></div>
<div class="abs foot-rule"></div>
<p class="abs copy">© 2021 BRIARLOOM . All Rights Reserved.</p>

</body>
</html>
```